"Precision Solutions for Aerospace Industries" product catalog Brennicor

General Catalog Guidelines
Format: A4, in vertical or horizontal orientation.
Cover Page: Should include the company logo, slogan, and website address (e.g., www.brennicor-example.com).
Layout: Each page can feature 1, 2, or up to 3 products, ensuring clarity and readability.
Catalog Content
1. Title Page
Catalog Name: "Technical Consumables for Aerospace".
Company Logo: BrenniCor.
High-Quality Image: Related to the aerospace industry.
2. Table of Contents
List of sections with corresponding page numbers for easy navigation.
3. Introduction / Scope of Activities
Company Overview: Brief introduction to BrenniCor's operations.
Specialization: Emphasis on manufacturing spare parts and consumables for special processes such as thermal spraying, diffusion brazing, welding, etc.
Certifications: Company certifications (AS9100, military concession) and a list of major clients.
Mission: "Brennicor's mission is to meet the requirements of thermal spray and aviation industry customers by continuous improvement of employees' qualifications, machining of difficult-to-machine materials using modern and non-conventional manufacturing processes, and new implementations of technological processes using developed know-how."
Vision: "To be a recognizable brand in the thermal spray and aviation industry on the global market. Be not only associated with the manufacturing of parts under the customers' purchase orders but also with innovative solutions that will bring many benefits to the contractor."
4. Key Sections of the Catalog
Consumables for Special Processes

Test coupons, panels, samples, and other elements for thermal spraying, chemical processing, welding.
Machining of difficult-to-machine materials such as nickel and cobalt-based superalloys, titanium, and hardened steel.
Reusable silicone masking and other masking solutions.
Coupons Regeneration

Description of the coupon regeneration process and its benefits (material savings, cost reduction, environmental impact).
Metal Parts and PSP Prefabricates

Structural elements, e.g., honeycombs, repair parts for turbines, ready-made PSP elements.
Machining and Support Services

Wire EDM cutting – benefits and applications.
Coating evaluation laboratory and technological accessories.
Consultations on technological processes, preparation for QUALTEX certification.
Modern Aviation Materials

Ceramic composites (CMC), nickel and cobalt-based superalloys, and other aerospace materials.
Repair and R&D Services

Examples of research and development projects (e.g., repair of Varnel 53 airfoils).
Solutions for issues related to thermal spraying and process optimization.
Additional Information

Information on hybrid additive manufacturing.
Current company status and client list.
5. Last Page
Contact Information:
Production Site: Wiktora Grabca 12, 05-410 Otwock, Poland.
R&D Center: Brzozówka 318B, 36-014 Brzozówka, Poland.
Email address, phone number, and social media links.
"Nice to Have" Elements
Inspirational Images: Products in use, e.g., aerospace tests, industrial applications
Updates

Project details can be found at this link https://files.example-share.net/t-KmQ4rwzLxa

Target Market(s)

aviation industry, metallurgy

Industry/Entity Type

Font styles to use
Sans Serif

Colors
0054AA
0677BA
7BADD7
CADEEF
E8F1F8
F0912C
F2A743
F7CA91
FBE8D2
FDF5EE

Requirements
Must have
• 1. Cover Eye-catching graphics. Your company logo. A short, clear title (e.g. catalog name, season, offer). 2. Table of contents Particularly important in larger catalogs. Makes it easier to quickly find individual sections. 3. Introduction / Company information A short company mission or introduction (information at https://brennicor-example.com/about-us/) 4. Key categories and sections Division into easy-to-understand sections, e.g.: Products, Services. 5. Product pages; 8. Aesthetics and readability Use colors consistent with the brand's visual identification. Consistent fonts and text hierarchy (e.g. titles larger than descriptions). Well-placed elements on the page so as not to overwhelm the viewer.
Nice to have
• Lifestyle inspirations and photos Photos from the industry such as: airplanes, turbines, lathe machines, WEDEM.

```html
<!DOCTYPE html>
<html lang="en">
<head>
<meta charset="UTF-8">
<title>Brennicor – Technical Consumables for Aerospace</title>
<link rel="stylesheet" href="https://fonts.googleapis.com/css2?family=Oswald:wght@300;400;500;600&display=swap">
<style>
  :root {
    --stage: #0d0d0d;
    --navy: #3a55a0;
    --navy-dark: #2c4487;
    --ink: #2b3f86;
    --white: #ffffff;
    --grey-footer: #8c8c8c;
    --pill-text: #6e6e6e;
    --body-ink: #3d58a4;
    --sky-orange: #f0912c;
    --sky-amber: #f2a743;
    --sky-red: #d8262c;
    --tarmac: #4a2318;
  }
  * { box-sizing: border-box; margin: 0; padding: 0; }
  html, body { width: 1199px; height: 1200px; overflow: hidden; background: var(--stage); }
  body { font-family: "Oswald", "Arial Narrow", sans-serif; }

  .page {
    position: absolute; left: 175px; top: 0;
    width: 850px; height: 1200px;
    background: var(--navy); overflow: hidden;
  }

  /* cover photo area */
  .hero { position: absolute; left: 0; top: 0; width: 850px; height: 565px; }
  .hero-photo {
    position: absolute; inset: 0;
    background:
      linear-gradient(180deg, rgba(0,0,0,0) 55%, rgba(40,15,10,.85) 100%),
      linear-gradient(90deg, var(--sky-orange) 0%, var(--sky-amber) 30%, #e2562a 55%, var(--sky-red) 80%, #f6b04a 100%);
  }
  .hero-tint {
    position: absolute; left: 294px; top: 0; width: 524px; height: 445px;
    background: rgba(200, 20, 40, .28);
  }
  .brand-box {
    position: absolute; left: 0; top: 39px; width: 400px; height: 83px;
    background: var(--white);
    display: flex; align-items: center; gap: 16px; padding-left: 48px;
  }
  .brand-mark { width: 40px; height: 40px; background: var(--ink); }
  .brand-name { font-size: 40px; font-weight: 500; color: var(--ink); letter-spacing: .5px; }

  .hero-title {
    position: absolute; right: 70px; top: 160px;
    text-align: right; color: var(--white); font-weight: 400; line-height: 1;
    text-transform: uppercase;
  }
  .hero-title .l1 { display: block; font-size: 104px; letter-spacing: 1px; }
  .hero-title .l2 { display: block; font-size: 80px; margin-top: 10px; }
  .hero-title .l3 { display: block; font-size: 76px; margin-top: 12px; }

  /* intro */
  .intro {
    position: absolute; left: 47px; top: 592px; width: 740px;
    color: var(--white); font-weight: 300; font-size: 15.5px; line-height: 1.33;
  }
  .intro p + p { margin-top: 18px; }

  .section-pill {
    position: absolute; left: 198px; top: 759px; width: 452px; height: 50px;
    background: var(--white); border-radius: 25px;
    box-shadow: 0 10px 14px -6px rgba(0,0,0,.35);
    display: flex; align-items: center; justify-content: center;
    color: var(--pill-text); font-size: 25px; font-weight: 400; text-transform: uppercase;
  }

  /* service cards */
  .card { position: absolute; top: 834px; width: 379px; height: 285px; }
  .card-left { left: 40px; }
  .card-right { left: 430px; }
  .card svg.card-shape { position: absolute; inset: 0; }
  .card-icon {
    position: absolute; left: 12px; top: 10px; width: 96px; height: 96px;
    border-radius: 50%; border: 4px solid var(--white);
  }
  .card-left .card-icon { background: radial-gradient(circle, #f2f2f4 0%, #d4d6dc 100%); }
  .card-right .card-icon { background: radial-gradient(circle, #f4f5f8 0%, #dfe3ec 100%); }
  .card-title {
    position: absolute; left: 22px; top: 121px;
    font-size: 17px; font-weight: 600; text-transform: uppercase;
  }
  .card-text {
    position: absolute; left: 22px; top: 158px; width: 335px;
    font-size: 13px; font-weight: 300; line-height: 1.3; text-align: justify;
  }
  .card-left .card-title, .card-left .card-text { color: var(--white); }
  .card-right .card-title, .card-right .card-text { color: var(--body-ink); }

  .footer {
    position: absolute; left: 0; top: 1109px; width: 850px; height: 91px;
    background: var(--grey-footer);
    display: flex; align-items: center; justify-content: center; padding-top: 6px;
    color: var(--white); font-size: 17px; font-weight: 500; letter-spacing: 1px;
  }
</style>
</head>
<body>
<main class="page">
  <header class="hero">
    <div class="hero-photo" role="img" aria-label="Business jet parked on the apron at sunset with an airport control tower behind it"></div>
    <div class="hero-tint"></div>
    <div class="brand-box">
      <span class="brand-mark"></span>
      <span class="brand-name">BrenniCor</span>
    </div>
    <h1 class="hero-title">
      <span class="l1">Technical</span>
      <span class="l2">Consumables</span>
      <span class="l3">for Aerospace</span>
    </h1>
  </header>

  <section class="intro">
    <p>Brennicor specializes in manufacturing, spare parts details &amp; consumable materials used in special processes such as thermal spraying, hardfacing, brazing, welding, chemical processing, and more. We also produce tooling for testing aerospace materials and coatings.</p>
    <p>Our primary customers include manufacturers of new engine components &amp; maintenance, repair, and overhaul (MRO) facilities worldwide. Our production facility is AS9100 certified, and we hold a military license.</p>
  </section>

  <h2 class="section-pill">Consumables for special processes</h2>

  <article class="card card-left">
    <svg class="card-shape" width="379" height="285" viewBox="0 0 379 285">
      <path d="M2,60 A56,56 0 0 1 58,4 H66 A56,56 0 0 1 118,40 C124,56 132,60 150,60 H349 A28,28 0 0 1 377,88 V255 A28,28 0 0 1 349,283 H30 A28,28 0 0 1 2,255 Z" fill="none" stroke="#ffffff" stroke-width="2"/>
    </svg>
    <div class="card-icon" role="img" aria-label="Machined test coupons and substrate samples"></div>
    <h3 class="card-title">Coupons &amp; substrates machining</h3>
    <p class="card-text">We specialize in manufacturing high-quality test coupons substrates specimens samples, buttons, panels, discs, and strips for thermal spray, cold spray, chemical processing &amp; welding applications in the aviation industry. Our range of materials includes nickel and cobalt-based superalloys, titanium, hardened steel, and aluminum alloys</p>
  </article>

  <article class="card card-right">
    <svg class="card-shape" width="379" height="285" viewBox="0 0 379 285">
      <path d="M0,60 A58,58 0 0 1 58,2 H66 A58,58 0 0 1 120,40 C126,56 134,60 152,60 H349 A30,30 0 0 1 379,90 V255 A30,30 0 0 1 349,285 H30 A30,30 0 0 1 0,255 Z" fill="#ffffff"/>
    </svg>
    <div class="card-icon" role="img" aria-label="Coated coupon restored to a clean coupon"></div>
    <h3 class="card-title">Coupons regeneration</h3>
    <p class="card-text">Our regeneration service restores coated coupons to their original specifications. By using mechanical stripping processes, we offer a faster and more cost effective alternative to producing new coupons This results in significant savings raw materials and heat treatment, while also reducing waste</p>
  </article>

  <footer class="footer">www.brennicor-example.com</footer>
</main>
</body>
</html>
```